Upmarket Bathroom and Kitchen ware supplier needs a classy business card design

We are a company based in Fiji, we sell plumbing ware (Kitchen and bathroom taps, Basins,showers, toilets etc) through up market show rooms to individuals and directly through Architects and designers of resorts and holiday houses for new builds and renovations. we are wanting to upgrade our over all look and brand. we are starting with a new logo but will be rebranding the whole business. This project is for a business card design for my management and tales team I would like it to be dark, classy and interesting

Target Market(s)

Resort directors and Management, High end holiday home owners

Contact Information for Business Card

Neil Dawson
Director
+64219473815

Colors

Designer to choose colors to be used in the design.

Requirements
Must have
• Must have an upmarket appearance I like darker charcoal shades but will be guided by the designers
• Please any catch phrases like "Crafting remarkable living rooms" this belongs tpo one of our suppliers so can not be used.
Nice to have
• Double sided, so front dedicated to logo provided and back info about the business and the person.

```html
<!DOCTYPE html>
<html lang="en">
<head>
<meta charset="utf-8">
<title>Business Card – Lagoon Interiors</title>
<link href="https://fonts.googleapis.com/css2?family=Lato:wght@700&family=Open+Sans:wght@400;600&display=swap" rel="stylesheet">
<style>
  :root {
    --backdrop: #3a2a1e;
    --kraft-light: #dcb688;
    --kraft-mid: #c99e6e;
    --kraft-dark: #b88a5a;
    --ink: #1a1410;
    --rule: rgba(26, 20, 16, 0.55);
  }
  * { margin: 0; padding: 0; box-sizing: border-box; }
  html, body {
    width: 1200px;
    height: 900px;
    overflow: hidden;
    background: var(--backdrop);
  }
  .canvas {
    position: relative;
    width: 1200px;
    height: 900px;
  }
  .card {
    position: absolute;
    left: 330px;
    width: 557px;
    height: 343px;
    background: linear-gradient(135deg, var(--kraft-light) 0%, var(--kraft-mid) 55%, var(--kraft-dark) 100%);
    color: var(--ink);
    text-align: center;
    font-family: "Open Sans", Arial, sans-serif;
  }
  .card--back { top: 90px; }
  .card--front { top: 470px; }

  .person-name {
    position: absolute;
    top: 64px;
    left: 0;
    width: 100%;
    font-family: "Lato", Arial, sans-serif;
    font-weight: 700;
    font-size: 21px;
    letter-spacing: 0.2px;
    text-transform: uppercase;
  }
  .person-role {
    position: absolute;
    top: 86px;
    left: 0;
    width: 100%;
    font-size: 16px;
  }
  .divider {
    position: absolute;
    left: 181px;
    width: 195px;
    height: 1px;
    background: var(--rule);
  }
  .divider--upper { top: 117px; }
  .divider--lower { top: 222px; }

  .contact-list {
    position: absolute;
    top: 129px;
    left: 0;
    width: 100%;
    list-style: none;
    font-size: 16px;
    line-height: 20px;
  }
  .contact-list .label { font-weight: 600; }

  .address {
    position: absolute;
    top: 239px;
    left: 0;
    width: 100%;
    font-size: 16px;
    line-height: 20px;
    font-style: normal;
  }

  .brand {
    position: absolute;
    top: 188px;
    left: 0;
    width: 100%;
  }
  .brand-mark {
    display: block;
    margin: 0 auto 22px;
  }
  .brand-name {
    font-size: 20px;
    font-weight: 400;
    letter-spacing: 7px;
    text-transform: uppercase;
  }
</style>
</head>
<body>
<main class="canvas">
  <section class="card card--back" aria-label="Card back with contact details">
    <h1 class="person-name">Jonah Whitfield</h1>
    <p class="person-role">Managing Director</p>
    <div class="divider divider--upper"></div>
    <ul class="contact-list">
      <li><span class="label">P:</span> 044-518 302 774</li>
      <li><span class="label">M:</span> 044-726 915 408</li>
      <li><span class="label">E:</span> jonah@lagoonint.com</li>
      <li><span class="label">W:</span> www.lagoonint.com</li>
    </ul>
    <div class="divider divider--lower"></div>
    <address class="address">48, Harbour View Road<br>Suva, Fiji, 679012.</address>
  </section>

  <section class="card card--front" aria-label="Card front with company name">
    <div class="brand">
      <svg class="brand-mark" width="18" height="18" viewBox="0 0 18 18" aria-hidden="true">
        <circle cx="9" cy="9" r="7.5" fill="none" stroke="#1a1410" stroke-width="1.5"/>
      </svg>
      <p class="brand-name">Lagoon Interiors</p>
    </div>
  </section>
</main>
</body>
</html>
```